Domestic violence resource cards for distribution to at-risk patients in an emergency department

Using the attached image(or very similar) and text document, a tri-fold business card is requested that integrates the image on the outside and the document content throughout the card's remaining faces. A creative format is requested, one that does not look like the typical cold, uncaring bullet point outlines that are found in similar resource projects. Bold or larger font sizes are requested for headings and body text is not required to be aligned or justified and the bullet points in the supplied document can be removed for creative license. Palattes should be clear, avoiding neons or implied target gender. Legibility is paramount, but again a creative presentation of a very serious subject is our goal. These cards are intended to be distributed to patients or others in the emergency department that may benefit from domestic violence resources. The business card size is mandatory so that the card can be concealed if needed by the receiver.
Updates

Reason: There are several revisions from designers that we are anxiously awaiting; we want to provide time for these designers to submit new designs but also continue spending time with their families and friends around the holiday season.

Target Market(s)

Patients and family in contact with emergency services

Industry/Entity Type

Healthcare

Contact Information for Business Card

Double sided tri-fold card with image on outer sides, text content and resource phone numbers on the exterior. When complete, the card should fold to standard US business card size.

Font styles to use
Other font styles liked:
• Designer's choice, but clear and legible

Requirements
Must have
• See above description. Card must be tri-fold, fold down to standard business card size, remain easily readable, and fold along the long edge.
Should not have
• Cartoon images; bloated fonts or clipart; bright, flashy neon or rainbow-like colors; additional graphics or charts.

```html
<!DOCTYPE html>
<html lang="en">
<head>
<meta charset="utf-8">
<title>Domestic Violence Resource Card</title>
<link href="https://fonts.googleapis.com/css2?family=Lato:wght@400;700&family=Montserrat:wght@700;800&display=swap" rel="stylesheet">
<style>
  :root {
    --bg: #e6e6e6;
    --card: #0b0b0b;
    --green: #8cc63f;
    --red: #d1141c;
    --white: #f4f4f4;
    --grey: #bdbdbd;
  }
  html, body {
    margin: 0;
    width: 1200px;
    height: 900px;
    overflow: hidden;
    background: radial-gradient(circle at 50% 45%, #f7f7f7 0%, var(--bg) 60%, #bcbcbc 100%);
    font-family: "Lato", Arial, sans-serif;
  }
  .card {
    position: absolute;
    left: 230px;
    top: 50px;
    width: 740px;
    height: 800px;
    box-shadow: 0 12px 30px rgba(0,0,0,.35);
  }
  .panel {
    position: relative;
    width: 740px;
    height: 400px;
    background: var(--card);
    overflow: hidden;
  }
  .fold-line {
    position: absolute;
    left: 0; right: 0; top: 399px;
    height: 2px;
    background: #262626;
    z-index: 2;
  }
  /* Outer panel — printed upside down so it reads correctly when folded */
  .panel--outer { transform: rotate(180deg); }
  .cover-photo {
    position: absolute;
    left: 0; top: 0;
    width: 420px; height: 400px;
    background: radial-gradient(ellipse at 55% 50%, #9a9a9a 0%, #4a4a4a 40%, #0b0b0b 75%);
  }
  .cover-mark {
    position: absolute;
    right: 0; top: 0;
    width: 40px; height: 40px;
    background: var(--red);
  }
  .cover-title {
    position: absolute;
    right: 46px;
    bottom: 60px;
    text-align: left;
    font-family: "Montserrat", Arial, sans-serif;
    font-weight: 800;
    line-height: 1;
  }
  .cover-title__main {
    display: block;
    color: var(--white);
    font-size: 40px;
    letter-spacing: 1px;
  }
  .cover-title__sub {
    display: block;
    color: var(--red);
    font-size: 19px;
    letter-spacing: .5px;
    margin-top: 4px;
  }
  /* Inner panel — resource list */
  .resources { padding: 48px 46px 0 46px; }
  .resources__title {
    margin: 0;
    font-family: "Montserrat", Arial, sans-serif;
    font-weight: 800;
    font-size: 37px;
    letter-spacing: .5px;
    color: var(--white);
    line-height: 1;
  }
  .resources__title em { font-style: normal; color: var(--green); }
  .resources__rule {
    height: 2px;
    background: var(--red);
    margin-top: 12px;
    width: 620px;
  }
  .resources__contact {
    text-align: right;
    width: 620px;
    color: var(--white);
    font-size: 14px;
    margin-top: 5px;
  }
  .resources__body {
    display: flex;
    justify-content: space-between;
    margin-top: 12px;
    width: 648px;
  }
  .resources__names, .resources__numbers {
    list-style: none;
    margin: 0; padding: 0;
    font-size: 17px;
    line-height: 21.5px;
  }
  .resources__names { color: var(--green); }
  .resources__numbers { color: var(--white); font-size: 15.5px; }
  .resources__footer {
    position: absolute;
    left: 46px; right: 46px; bottom: 34px;
    display: flex;
    align-items: center;
    gap: 20px;
    color: var(--white);
    font-size: 14px;
  }
  .resources__footer span.line {
    flex: 1;
    height: 1px;
    background: var(--grey);
  }
</style>
</head>
<body>
  <div class="card">
    <section class="panel panel--outer">
      <div class="cover-photo" role="img" aria-label="Black and white photo of two clenched fists bound together with rope"></div>
      <div class="cover-mark"></div>
      <div class="cover-title">
        <span class="cover-title__main">DOMESTIC</span>
        <span class="cover-title__sub">VIOLENCE RESOURCE</span>
      </div>
    </section>
    <div class="fold-line"></div>
    <section class="panel panel--inner">
      <div class="resources">
        <h1 class="resources__title">DOMESTIC <em>VIOLENCE RESOURCE</em></h1>
        <div class="resources__rule"></div>
        <div class="resources__contact">Contact us</div>
        <div class="resources__body">
          <ul class="resources__names">
            <li>National Safe Home Hotline</li>
            <li>Shelter Point Denver: Domestic Violence Crisis Resource</li>
            <li>Crossroads Domestic Violence Resources</li>
            <li>The Harbor Center</li>
            <li>Kinfolk Circle Violence Resources</li>
            <li>Green Bench: Sexual Assault Victim's Advocate</li>
            <li>Heart Is Safe: Teen Dating Resource</li>
            <li>Or text "heartis" to</li>
          </ul>
          <ul class="resources__numbers">
            <li>1-800-555-0101</li>
            <li>303-555-0142</li>
            <li>303-555-0178</li>
            <li>1-888-555-0190</li>
            <li>303-555-0113</li>
            <li>303-555-0166</li>
            <li>1-866-555-0127</li>
            <li>55123</li>
          </ul>
        </div>
      </div>
      <div class="resources__footer">
        <span class="line"></span>
        <span>www.safehavenlist.org</span>
        <span class="line"></span>
      </div>
    </section>
  </div>
</body>
</html>
```